Keelstone Advisory - Careerloom Header

I am a solopreneur with a consulting company. I do management consulting for small and mid-size manufacturers. There are two ways my prospects check me out - my web page, which went live this week (www.keelstoneadvisory.example), and my personal Careerloom page. I'm working on my Careerloom page now, and I'd like to have a header image that is unique and aligned with my brand.

My clients are smaller manufacturers, typically with 50-400 people. They are privately held, often by an individual or family, but sometimes by a professional investment group. They aren't as sophisticated as the Corvane 300 guys, and sometimes they struggle to grow because their processes break, or they don't have the right people or something else like that. I help them get through those issues.

Many of the people visiting the site will have a technical/engineering orientation, and most are in their late 40's to early 60's.

From my research, I think the image for my personal page is 1584x396, and this will be my primary page. The business page has a banner image size of 1536x768. I'd like to be able to use the same image in both.

Target Market(s)

Small and Mid-size manufacturers - C-Suite executives

Industry/Entity Type

Manufacturing

Font styles to use
Sans Serif

Colors

Designer to choose colors to be used in the design.

Requirements
Must have
• Logo incorporated. Be adaptable to both my personal Careerloom page and Business page, which have slightly different sizes.

```html
<!DOCTYPE html>
<html lang="en">
<head>
<meta charset="utf-8">
<title>Keelstone Advisory – Careerloom Header Variants</title>
<link rel="stylesheet" href="https://fonts.googleapis.com/css2?family=Open+Sans:wght@400;600;700&display=swap">
<style>
  :root {
    --stage: #e6edf2;
    --paper: #ffffff;
    --navy: #22296b;
    --royal: #414fb0;
    --amber: #df962e;
    --ink: #2d2d2d;
    --rule: #9a9a9a;
    --label: #333333;
  }
  * { margin: 0; padding: 0; box-sizing: border-box; }
  html, body {
    width: 1095px; height: 1200px; overflow: hidden;
    background: var(--stage);
    font-family: "Open Sans", Arial, sans-serif;
  }
  .canvas { position: relative; width: 1095px; height: 1200px; }

  .size-label {
    position: absolute; transform: translateX(-50%);
    font-size: 27px; font-weight: 400; color: var(--label); white-space: nowrap;
  }
  .size-label--profile { left: 565px; top: 120px; }
  .size-label--business { left: 516px; top: 590px; }

  .banner { position: absolute; background: var(--paper); overflow: hidden; }
  .banner--profile { left: 53px; top: 185px; width: 989px; height: 246px; }
  .banner--business { left: 148px; top: 644px; width: 796px; height: 399px; }
  .banner__shapes { position: absolute; inset: 0; width: 100%; height: 100%; }

  .brand { position: absolute; left: 20px; top: 92px; display: flex; align-items: center; gap: 14px; }
  .brand__dot { width: 40px; height: 40px; border-radius: 50%; background: var(--navy); }
  .brand__name {
    font-size: 23px; font-weight: 600; line-height: 1.05; color: var(--navy);
  }

  .copy { position: absolute; color: var(--ink); }
  .copy__title { font-weight: 700; letter-spacing: -0.2px; white-space: nowrap; }
  .copy__title .accent { color: var(--navy); }
  .copy__text { font-weight: 400; }

  .banner--profile .copy { top: 58px; width: 215px; }
  .banner--profile .copy__title { font-size: 24px; line-height: 30px; margin-bottom: 2px; }
  .banner--profile .copy__text { font-size: 13.5px; line-height: 17.5px; }
  .copy--left { left: 451px; }
  .copy--right { left: 745px; }
  .divider { position: absolute; left: 696px; top: 29px; width: 1px; height: 151px; background: var(--rule); }

  .banner--business .copy { left: 405px; top: 72px; width: 290px; }
  .banner--business .copy__title { font-size: 33px; line-height: 42px; margin-bottom: 8px; }
  .banner--business .copy__text { font-size: 17.5px; line-height: 23px; }
  .banner--business .copy__text + .copy__text { margin-top: 22px; }
</style>
</head>
<body>
<main class="canvas">
  <p class="size-label size-label--profile">1584 x 396</p>

  <section class="banner banner--profile" aria-label="Personal page header, 1584 by 396">
    <svg class="banner__shapes" viewBox="0 0 728 181" preserveAspectRatio="none" aria-hidden="true">
      <polygon points="153,0 213,0 288,181 247,181" fill="var(--navy)"/>
      <polygon points="234,76 285,76 327,153 728,153 728,181 272,181" fill="var(--amber)"/>
    </svg>

    <div class="brand">
      <span class="brand__dot"></span>
      <span class="brand__name">Keelstone<br>Advisory</span>
    </div>

    <div class="copy copy--left">
      <h2 class="copy__title">BUSINESS <span class="accent">PAGE</span></h2>
      <p class="copy__text">Lorem ipsum lorem ipsum, lorem ipsum lorem ipsum lorem ipsum lorem ipsum lorem ipsum</p>
    </div>
    <span class="divider"></span>
    <div class="copy copy--right">
      <h2 class="copy__title">BUSINESS <span class="accent">PAGE</span></h2>
      <p class="copy__text">Lorem ipsum lorem ipsum, lorem ipsum lorem ipsum lorem ipsum lorem ipsum lorem ipsum</p>
    </div>
  </section>

  <p class="size-label size-label--business">1536 x 768</p>

  <section class="banner banner--business" aria-label="Business page banner, 1536 by 768">
    <svg class="banner__shapes" viewBox="0 0 586 294" preserveAspectRatio="none" aria-hidden="true">
      <polygon points="0,0 104,0 211,294 109,294" fill="var(--royal)"/>
      <polygon points="130,0 160,0 273,294 211,294" fill="var(--navy)"/>
      <polygon points="104,0 161,0 51,294 0,294" fill="var(--amber)"/>
    </svg>

    <div class="copy">
      <h2 class="copy__title">BUSINESS <span class="accent">PAGE</span></h2>
      <p class="copy__text">Lorem ipsum lorem ipsum, lorem ipsum lorem ipsum lorem lorem ipsum lorem ipsum.</p>
      <p class="copy__text">Lorem ipsum lorem ipsum, lorem ipsum lorem ipsum lorem lorem ipsum lorem ipsum</p>
    </div>
  </section>
</main>
</body>
</html>
```